Quiet Harbor Candle Company needs a Label design

We need a label design for a new candle company based in Charleston South Carolina. Our mission is to provide people with candles that will fill any space with fragrances that are uplifting, comforting, fresh and will make any space feel like home. Our candles are aromatherapy, 100% soy wax, and hand poured (we would love for this to be indicated somewhere on the label). We would like to see a label that is modern, very clean and uses pastel colors like green, blush pink, mauve and blush blue. The final design should communicate peace, gratitude, hope, and happiness.

```html
<!DOCTYPE html>
<html lang="en">
<head>
<meta charset="utf-8">
<title>Quiet Harbor Candle Company – Labels and Box</title>
<link href="https://fonts.googleapis.com/css2?family=Libre+Baskerville:wght@700&family=Quicksand:wght@400;500&family=Josefin+Sans:wght@400&display=swap" rel="stylesheet">
<style>
  :root{
    --page:#f3f3f3;
    --paper:#ffffff;
    --mauve:#b493bb;
    --honey:#ebc472;
    --blush-blue:#90a4b1;
    --sage:#9fb59d;
    --box:#b3c1c8;
    --box-label:#99a9b2;
    --ink:#3d4246;
    --ink-soft:#5c666c;
    --brand-grey:#8796a0;
    --cut:#d6237a;
    --fold:#39b4e6;
    --warn:#f2d21b;
  }
  *{margin:0;padding:0;box-sizing:border-box}
  html,body{width:967px;height:1200px;overflow:hidden;background:var(--page)}
  .canvas{position:relative;width:967px;height:1200px;background:var(--page)}

  .label-row{position:absolute;top:170px;left:47px;display:flex;gap:24px}
  .label{position:relative;width:200px;height:150px;color:var(--ink);text-align:center}
  .label--mauve{background:var(--mauve)}
  .label--honey{background:var(--honey)}
  .label--blue{background:var(--blush-blue)}
  .label--sage{background:var(--sage)}
  .label__frame{position:absolute;inset:6px;border:2px solid rgba(255,255,255,.75)}
  .label__mark{position:absolute;top:22px;left:50%;width:12px;height:12px;margin-left:-6px;border-radius:50%;background:var(--ink)}
  .label__brand{position:absolute;top:42px;left:0;right:0;font:400 14px "Quicksand",sans-serif;letter-spacing:.3px}
  .label__scent{position:absolute;top:86px;left:0;right:0;font:700 18px "Libre Baskerville",serif;letter-spacing:.5px}
  .label__notes{position:absolute;top:112px;left:0;right:0;font:400 8.5px "Josefin Sans",sans-serif;letter-spacing:.6px}

  .dieline{position:absolute;left:0;top:512px;width:967px;height:688px}
  .box-body{fill:var(--box);stroke:var(--box);stroke-width:70;stroke-linejoin:round}
  .cut-line{fill:none;stroke:var(--cut);stroke-width:1.3}
  .fold-line{fill:none;stroke:var(--fold);stroke-width:1;stroke-dasharray:3 3}
  .t-brand{font-family:"Quicksand",sans-serif;font-size:15px;fill:var(--brand-grey);text-anchor:middle}
  .t-brand--large{font-size:20px}
  .brand-dot{fill:var(--brand-grey)}
  .t-head{font-family:"Quicksand",sans-serif;font-weight:500;font-size:8px;fill:var(--ink);text-anchor:middle}
  .t-body{font-family:"Quicksand",sans-serif;font-size:6.4px;fill:var(--ink-soft);text-anchor:middle}
  .t-left{text-anchor:start}
  .t-scent{font-family:"Libre Baskerville",serif;font-weight:700;font-size:16px;fill:var(--ink);text-anchor:middle}
  .t-notes{font-family:"Josefin Sans",sans-serif;font-size:7px;fill:var(--ink);text-anchor:middle}
  .box-label{fill:var(--box-label)}
  .box-label__frame{fill:none;stroke:#d3dbdf;stroke-width:1.2}
  .badge{fill:none;stroke:var(--ink-soft);stroke-width:1}
  .warn{fill:var(--warn);stroke:var(--ink);stroke-width:1}
  .warn-mark{stroke:var(--ink);stroke-width:1.4}
  .social-dot{fill:var(--ink)}
</style>
</head>
<body>
<main class="canvas">

  <section class="label-row" aria-label="Candle jar labels">
    <article class="label label--mauve">
      <div class="label__frame"></div><span class="label__mark"></span>
      <p class="label__brand">Quiet Harbor</p>
      <h2 class="label__scent">BIRCHWOOD</h2>
      <p class="label__notes">Pear + Lavander + Rose</p>
    </article>
    <article class="label label--honey">
      <div class="label__frame"></div><span class="label__mark"></span>
      <p class="label__brand">Quiet Harbor</p>
      <h2 class="label__scent">TANGERINE</h2>
      <p class="label__notes">Ginger + Lavander + Rose</p>
    </article>
    <article class="label label--blue">
      <div class="label__frame"></div><span class="label__mark"></span>
      <p class="label__brand">Quiet Harbor</p>
      <h2 class="label__scent">GRAPEFRUIT</h2>
      <p class="label__notes">Sage + Lavander + Rose</p>
    </article>
    <article class="label label--sage">
      <div class="label__frame"></div><span class="label__mark"></span>
      <p class="label__brand">Quiet Harbor</p>
      <h2 class="label__scent">BIRCHWOOD</h2>
      <p class="label__notes">Pear + Lavander + Rose</p>
    </article>
  </section>

  <svg class="dieline" viewBox="0 640 1209 860" aria-label="Candle box dieline">
    <path class="box-body" d="M180,998 L143,1003 L143,1200 L180,1212 L290,1260 L283,1295 L405,1295 L405,1212 L450,1380 L585,1380 L630,1212 L855,1212 L855,1362 L895,1362 L905,1318 L1030,1318 L1040,1362 L1078,1362 L1078,775 L1062,775 L1062,740 Q1062,727 1048,727 L885,727 Q871,727 871,740 L871,775 L855,775 L855,998 L830,893 L648,893 L630,998 L530,998 Q518,1015 506,998 L405,998 L388,893 L208,893 Z"/>
    <path class="cut-line" d="M180,998 L143,1003 L143,1200 L180,1212 L290,1260 L283,1295 L405,1295 L405,1212 L450,1380 L585,1380 L630,1212 L855,1212 L855,1362 L895,1362 L905,1318 L1030,1318 L1040,1362 L1078,1362 L1078,775 L1062,775 L1062,740 Q1062,727 1048,727 L885,727 Q871,727 871,740 L871,775 L855,775 L855,998 L830,893 L648,893 L630,998 L530,998 Q518,1015 506,998 L405,998 L388,893 L208,893 Z"/>
    <g class="fold-line">
      <line x1="180" y1="998" x2="1078" y2="998"/>
      <line x1="180" y1="1210" x2="1078" y2="1210"/>
      <line x1="855" y1="775" x2="1078" y2="775"/>
      <line x1="180" y1="998" x2="180" y2="1210"/>
      <line x1="405" y1="998" x2="405" y2="1210"/>
      <line x1="630" y1="998" x2="630" y2="1210"/>
      <line x1="855" y1="998" x2="855" y2="1210"/>
    </g>

    <g class="tuck-flap" transform="rotate(180 966 900)">
      <text class="t-brand t-brand--large" x="966" y="894">Quiet Harbor</text>
      <circle class="brand-dot" cx="966" cy="872" r="7"/>
    </g>

    <g class="panel-benefits">
      <text class="t-head" x="292" y="1088">Birchwood Benefits</text>
      <text class="t-body" x="292" y="1101">Soft notes of pear and lavender settle into a</text>
      <text class="t-body" x="292" y="1110">warm birch base, calming busy rooms and easing</text>
      <text class="t-body" x="292" y="1119">the mind. Burns clean and slow for long</text>
      <text class="t-body" x="292" y="1128">quiet evenings at home.</text>
    </g>

    <g class="panel-front">
      <circle class="brand-dot" cx="517" cy="1042" r="7"/>
      <text class="t-brand" x="517" y="1071">Quiet Harbor</text>
      <rect class="box-label" x="440" y="1104" width="155" height="57"/>
      <rect class="box-label__frame" x="444" y="1108" width="147" height="49"/>
      <text class="t-scent" x="517" y="1136">BIRCHWOOD</text>
      <text class="t-notes" x="517" y="1147">Pear + Lavander + Rose</text>
      <text class="t-body" x="517" y="1182">MADE IN SOUTH CAROLINA</text>
      <text class="t-body" x="517" y="1195">250g | 9.45 oz</text>
    </g>

    <g class="panel-story">
      <text class="t-head" x="742" y="1088">Scented Candle</text>
      <text class="t-body" x="742" y="1103">Hand Poured in Charleston South Carolina</text>
      <text class="t-body" x="742" y="1113">100% Essential Oil and Soy Wax</text>
      <circle class="badge" cx="673" cy="1143" r="14"/>
      <circle class="badge" cx="719" cy="1143" r="14"/>
      <circle class="badge" cx="765" cy="1143" r="14"/>
      <circle class="badge" cx="810" cy="1143" r="14"/>
    </g>

    <g class="panel-back">
      <circle class="brand-dot" cx="966" cy="1042" r="7"/>
      <text class="t-brand" x="966" y="1070">Quiet Harbor</text>
      <text class="t-body t-left" x="956" y="1163">www.quietharborcandles.com</text>
      <text class="t-body t-left" x="956" y="1177">Follow us on social media</text>
      <circle class="social-dot" cx="962" cy="1188" r="4.5"/>
      <circle class="social-dot" cx="975" cy="1188" r="4.5"/>
      <circle class="social-dot" cx="988" cy="1188" r="4.5"/>
      <text class="t-body t-left" x="997" y="1190">@quietharborcandles</text>
    </g>

    <g class="panel-safety">
      <path class="warn" d="M470,1233 L480,1251 L460,1251 Z"/>
      <line class="warn-mark" x1="470" y1="1239" x2="470" y2="1245"/>
      <circle class="badge" cx="472" cy="1273" r="11"/>
      <circle class="badge" cx="501" cy="1273" r="11"/>
      <circle class="badge" cx="531" cy="1273" r="11"/>
      <circle class="badge" cx="561" cy="1273" r="11"/>
      <circle class="badge" cx="472" cy="1305" r="11"/>
      <circle class="badge" cx="501" cy="1305" r="11"/>
      <circle class="badge" cx="531" cy="1305" r="11"/>
      <circle class="badge" cx="561" cy="1305" r="11"/>
      <text class="t-body" x="517" y="1341">Quiet Harbor Inc.</text>
      <text class="t-body" x="517" y="1348">Address, Street 99</text>
      <text class="t-body" x="517" y="1355">123 South Carolina</text>
    </g>
  </svg>

</main>
</body>
</html>
```